HiItsJonBrell.com needs a modern, eye-catching business card design

My name is Jon Brell and I own a video training (software development industry) website. I need a business card design that is eye catching for when I travel to conferences or do seminars. I would prefer something simple but bold. Something along the lines of this: https://pixvaultstatic.example/gallery_img/530172/44018/44018_9917302_530172_image.jpg

Note that I do not have a specific logo, but I do have an caricature I use on my site of myself. I've not attached it because I'm not really a fan of having it on my business cards. I would prefer lettering instead of an image. You can go to my website (https://hiitsjonbrell.com) for inspiration.

I want to add the following information on my card (the order of these, their size, and their casing is up to you):

Jon Brell
jon@HiItsJonBrell.com
@HiItsJonBrell
HiItsJonBrell.com
vidsharehub.example/HiItsJonBrell

I would also like to have somewhere on the card a small ad that says "Get a free course at https://HiItsJonBrell.com/FreeCourse". Feel free to play with that wording or layout if you need. I would prefer this text to be at the bottom of the card and subtle. Some small eye-catching thing might be ok but nothing huge or garish.

I plan on printing this card at pressquill.example (https://www.pressquill.example/us/design-guidelines/business-cards.html). I would like it to be the standard size (3.66" x 2.16"). I would prefer rounded corners and horizontal orientation. This is a two-side design. I would prefer the side with all of the information be primarily white but I like color text (again, flexible on that). On the front side, I like simple. Maybe just HiItsJonBrell.com (casing on that is up to you - whatever looks and reads the best - that goes for all of the casing). As for font choices, I prefer a modern, clean font. For example, Open Sans Light can be a nice option.

Website Info (might be helpful for the card):
Color Palette

Darkest blue - #263246
Alternate blue - #2F4E6A
Light blue - #2A98C3
Orange - #FF6201
White - #FFFFFF

Font for Jon Brell Logo

Jellyka Estryas Handwriting
http://www.typecrate.example/jellyka_estryas_handwriting.font

Fonts for Site Content and VidShare Thumbnails

Lovelo (bold title font)
http://www.glyphmill.example/lovelo-font/

Open Sans (body font)
http://www.letterbarn.example/fonts/open-sans

Industry/Entity Type

Software Development

Contact Information for Business Card

Jon Brell
jon@HiItsJonBrell.com
@HiItsJonBrell
HiItsJonBrell.com
vidsharehub.example/HiItsJonBrell

Get a free course at https://HiItsJonBrell.com/FreeCourse

Colors

Designer to choose colors to be used in the design.

Requirements
Nice to have
• Modern color - maybe primarily a color on the front and then that color as an accent on the back.
Should not have
• Lots of colors - I LOVE color but do not want a rainbow of colors on the card.

```html
<!DOCTYPE html>
<html lang="en">
<head>
<meta charset="utf-8">
<title>Jon Brell – Business Card</title>
<link rel="stylesheet" href="https://fonts.googleapis.com/css2?family=Montserrat:wght@400;500&family=Open+Sans:wght@400&display=swap">
<style>
  :root {
    --navy: #263246;
    --blue: #2F4E6A;
    --orange: #F7931E;
    --ad-orange: #FF6201;
    --white: #FFFFFF;
    --backdrop: #F1EEE8;
  }
  html, body {
    margin: 0;
    padding: 0;
    width: 1200px;
    height: 1194px;
    overflow: hidden;
    background: var(--backdrop);
  }
  .canvas {
    position: relative;
    width: 1200px;
    height: 1194px;
  }
  .card {
    position: absolute;
    left: 190px;
    width: 844px;
    height: 482px;
    display: block;
    border-radius: 10px;
    overflow: hidden;
  }
  .card--front { top: 64px; }
  .card--back { top: 640px; }

  .fill-white { fill: var(--white); }
  .fill-navy { fill: var(--navy); }
  .fill-blue { fill: var(--blue); }
  .fill-orange { fill: var(--orange); }
  .ring { fill: var(--white); fill-opacity: 0.22; }

  .wordmark {
    font-family: "Montserrat", sans-serif;
    font-weight: 500;
    font-size: 104px;
    letter-spacing: 1px;
  }
  .wordmark--front { fill: var(--orange); }
  .wordmark--back { fill: var(--white); }
  .front-url {
    font-family: "Montserrat", sans-serif;
    font-weight: 400;
    font-size: 23px;
    fill: var(--blue);
  }
  .contact-text {
    font-family: "Montserrat", sans-serif;
    font-weight: 400;
    font-size: 22px;
    fill: var(--blue);
  }
  .icon-line {
    fill: none;
    stroke: var(--white);
    stroke-width: 2.4;
    stroke-linejoin: round;
  }
  .ad-text {
    font-family: "Open Sans", sans-serif;
    font-weight: 400;
    font-size: 24px;
    fill: var(--ad-orange);
  }
</style>
</head>
<body>
<main class="canvas">

  <!-- Front side -->
  <svg class="card card--front" viewBox="0 0 1056 603" aria-label="Business card front">
    <defs>
      <clipPath id="front-clip"><rect width="1056" height="603"/></clipPath>
    </defs>
    <g clip-path="url(#front-clip)">
      <rect class="fill-white" width="1056" height="603"/>
      <polygon class="fill-navy" points="0,0 298,0 0,177"/>
      <polygon class="fill-blue" points="0,370 620,0 1056,0 1056,603 0,603"/>
      <polygon class="fill-navy" points="1056,232 1056,422 753,603 416,603"/>
      <polygon class="fill-white" points="1056,422 1056,603 753,603"/>
      <circle class="ring" cx="527" cy="300" r="375"/>
      <circle class="fill-white" cx="527" cy="300" r="272"/>
      <text class="wordmark wordmark--front" x="530" y="318" text-anchor="middle">Jon Brell</text>
      <text class="front-url" x="527" y="368" text-anchor="middle">HiItsJonBrell.com</text>
    </g>
  </svg>

  <!-- Back side -->
  <svg class="card card--back" viewBox="0 0 1056 603" aria-label="Business card back">
    <defs>
      <clipPath id="back-clip"><rect width="1056" height="603"/></clipPath>
    </defs>
    <g clip-path="url(#back-clip)">
      <rect class="fill-white" width="1056" height="603"/>

      <g class="header-bands">
        <polygon class="fill-navy" points="0,0 298,0 0,178"/>
        <polygon class="fill-blue" points="298,0 616,0 225,235 0,235 0,178"/>
        <polygon class="fill-navy" points="612,48 1056,48 1056,235 298,235"/>
        <text class="wordmark wordmark--back" x="1016" y="170" text-anchor="end">Jon Brell</text>
      </g>

      <g class="contact-list">
        <g class="contact contact--email">
          <circle class="fill-orange" cx="147" cy="337" r="26"/>
          <rect class="icon-line" x="132" y="326" width="30" height="21"/>
          <polyline class="icon-line" points="132,326 147,339 162,326"/>
          <line class="icon-line" x1="132" y1="347" x2="143" y2="336"/>
          <line class="icon-line" x1="162" y1="347" x2="151" y2="336"/>
          <text class="contact-text" x="190" y="343">jon@HiItsJonBrell.com</text>
        </g>
        <g class="contact contact--social">
          <circle class="fill-orange" cx="147" cy="415" r="26"/>
          <text class="contact-text" x="190" y="421">@HiItsJonBrell</text>
        </g>
        <g class="contact contact--web">
          <circle class="fill-orange" cx="625" cy="337" r="26"/>
          <circle class="icon-line" cx="625" cy="337" r="15"/>
          <ellipse class="icon-line" cx="625" cy="337" rx="6.5" ry="15"/>
          <line class="icon-line" x1="610" y1="337" x2="640" y2="337"/>
          <line class="icon-line" x1="613" y1="329" x2="637" y2="329"/>
          <line class="icon-line" x1="613" y1="345" x2="637" y2="345"/>
          <text class="contact-text" x="662" y="343">HiItsJonBrell.com</text>
        </g>
        <g class="contact contact--video">
          <circle class="fill-orange" cx="625" cy="415" r="26"/>
          <text class="contact-text" x="662" y="421">vidsharehub.example/HiItsJonBrell</text>
        </g>
      </g>

      <g class="footer-band">
        <rect class="fill-navy" x="0" y="513" width="1056" height="90"/>
        <polygon class="fill-white" points="837,513 907,513 760,603 690,603"/>
        <polygon class="fill-blue" points="907,513 1056,513 1056,603 760,603"/>
        <text class="ad-text" x="43" y="566">Get a free course at https://HiItsJonBrell.com/FreeCourse</text>
      </g>
    </g>
  </svg>

</main>
</body>
</html>
```